Brightwell Homes Guide Business card

I have had at the logo designed here and attached. The business compares off the plan apartments in Sydney and provides quick comparison for new home buyers e.g price, floor plans and location. I would like the complimentary colours used on the business card. I would like it be unique but also look professional. I also have a website to gain inspiration from www.brightwellhomesguide.com.au
Updates
Industry/Entity Type
Business
Contact Information for Business Card
Helen Vostrakis
Director of Business Development
e: helen.vostrakis@brightwellhomesguide.com.au
p: (02) 8143 7692
m: 0431 572 908
w: www.brightwellhomesguide.com.au
Look and feel
Each slider illustrates characteristics of the customer's brand and the style your logo design should communicate.

```html
<!DOCTYPE html>
<html lang="en">
<head>
<meta charset="utf-8">
<title>Brightwell Homes Guide – Business Card</title>
<link href="https://fonts.googleapis.com/css2?family=Lato:ital,wght@0,400;0,700;0,900;1,400&display=swap" rel="stylesheet">
<style>
  :root {
    --brand-green: #9bc44c;
    --brand-blue: #4a8fd6;
    --ink: #4a4a4a;
    --paper: #ffffff;
    --mark: #3a3a3a;
  }
  html, body {
    margin: 0;
    padding: 0;
    width: 1200px;
    height: 1199px;
    overflow: hidden;
    background: var(--paper);
    font-family: "Lato", Arial, sans-serif;
  }
  .sheet { position: relative; width: 1200px; height: 1199px; }
  .crop-marks { position: absolute; inset: 0; }
  .back-panel {
    position: absolute; left: 76px; top: 450px; width: 317px; height: 288px;
    background: var(--brand-green); color: var(--paper);
  }
  .back-panel .company {
    position: absolute; left: 44px; top: 120px; margin: 0;
    font-weight: 700; font-size: 14px; letter-spacing: 0.1px; line-height: 1;
  }
  .back-panel .web { position: absolute; left: 44px; top: 137px; font-weight: 700; font-size: 9.5px; }
  .back-panel .tagline { position: absolute; left: 44px; top: 150px; font-size: 9.3px; }
  .office {
    position: absolute; left: 418px; top: 560px; width: 100px;
    color: var(--brand-green); font-size: 10px; line-height: 13px; text-align: right;
  }
  .office .title { font-weight: 700; padding-right: 5px; }
  .office .row { display: flex; justify-content: space-between; }
  .office .label { font-weight: 700; }
  .side-tab { position: absolute; left: 0; top: 0; }
  .front-panel { position: absolute; left: 647px; top: 450px; width: 493px; height: 289px; }
  .brand {
    position: absolute; left: 161px; top: 43px; display: flex; align-items: center; gap: 8px;
    color: var(--brand-green); font-weight: 700; font-size: 19px; white-space: nowrap;
  }
  .brand .dot { width: 16px; height: 16px; background: var(--brand-blue); }
  .contact {
    position: absolute; left: 0; right: 0; top: 139px; text-align: center;
    color: var(--ink); font-size: 11.5px; line-height: 14px;
  }
  .contact .name { font-weight: 700; font-size: 17px; line-height: 20px; }
  .contact .position { font-style: italic; margin-bottom: 2px; }
  .front-band {
    position: absolute; left: 647px; top: 695px; width: 493px; height: 44px;
    background: var(--brand-green);
  }
</style>
</head>
<body>
<div class="sheet">
  <svg class="crop-marks" width="1200" height="1199" viewBox="0 0 1200 1199" aria-hidden="true">
    <g stroke="var(--mark)" stroke-width="0.8">
      <line x1="91" y1="430" x2="91" y2="456"/><line x1="91" y1="731" x2="91" y2="758"/>
      <line x1="55" y1="466" x2="82" y2="466"/><line x1="55" y1="722" x2="82" y2="722"/>
      <line x1="554" y1="430" x2="554" y2="456"/><line x1="554" y1="731" x2="554" y2="758"/>
      <line x1="563" y1="466" x2="590" y2="466"/><line x1="563" y1="722" x2="590" y2="722"/>
      <line x1="662" y1="430" x2="662" y2="456"/><line x1="662" y1="741" x2="662" y2="758"/>
      <line x1="626" y1="466" x2="654" y2="466"/><line x1="626" y1="722" x2="647" y2="722"/>
      <line x1="1125" y1="430" x2="1125" y2="456"/><line x1="1125" y1="741" x2="1125" y2="758"/>
      <line x1="1134" y1="466" x2="1161" y2="466"/><line x1="1140" y1="722" x2="1161" y2="722"/>
    </g>
    <polygon class="side-tab" points="541,512 567,502 567,688 541,676" fill="var(--brand-green)"/>
    <polygon points="801,452 986,452 977,478 810,478" fill="var(--brand-green)"/>
  </svg>

  <section class="back-panel">
    <h1 class="company">BRIGHTWELL HOMES GUIDE</h1>
    <div class="web">www.brightwellhomesguide.com.au</div>
    <div class="tagline">NEW APARTMENTS RIGHT AT YOUR DOOR STEP</div>
  </section>

  <address class="office" style="font-style:normal">
    <div class="title">Head Office</div>
    <div>418 Alder Lane NW</div>
    <div>Mount Ridley, LA</div>
    <div class="row"><span class="label">T</span><span>9781-240-6317</span></div>
    <div class="row"><span class="label">F</span><span>9782-316-4590</span></div>
  </address>

  <section class="front-panel">
    <div class="brand"><span class="dot"></span>Brightwell Homes Guide</div>
    <div class="contact">
      <div class="name">Your Name</div>
      <div class="position">Job Position</div>
      <div>Address: City, State, Zip</div>
      <div>Phone: (02) 8143 7692</div>
      <div>Mobile: 0431 572 908</div>
      <div>Email: enquiries@brightwellhomesguide.com.au</div>
    </div>
  </section>
  <div class="front-band"></div>
</div>
</body>
</html>
```